I need a better looking dashboard for my web application

I have a very table heavy web page that I would like to add a design touch to it. I have the logo and primary colors picked out, I just need some help in adding visual appeal the page. I would also like to add a couple of button to the page as shortcuts. Every spot that has a + sign could have a button added. I would also like to add another graph (the data will be in the uploaded files. Please feel free to ask any questions :-)

```html
<!DOCTYPE html>
<html lang="en">
<head>
<meta charset="UTF-8">
<title>Sub Management Dashboard</title>
<link href="https://fonts.googleapis.com/css2?family=Poppins:wght@400;500;600&display=swap" rel="stylesheet">
<style>
:root{
  --bg:#f4f4f5;
  --panel:#ffffff;
  --border:#e6e6ea;
  --ink:#1c1c28;
  --ink-soft:#555a66;
  --muted:#8a8f99;
  --navy:#1d1a6b;
  --primary:#2f2bb8;
  --indigo:#3a2ec4;
  --violet:#6c63e8;
  --lilac:#a59cf7;
  --sky:#3f7fdc;
  --active:#4a90e2;
  --purple-bar:#5e3290;
  --green-bar:#2ea84a;
  --red-bar:#dc3545;
  --logo-green:#2e7d32;
  --logo-border:#b5ebb5;
}
*{box-sizing:border-box;margin:0;padding:0}
html,body{width:1200px;height:675px;overflow:hidden}
body{font-family:"Poppins",sans-serif;background:var(--bg);color:var(--ink);position:relative}
.abs{position:absolute}

/* sidebar */
.sidebar{left:0;top:0;width:150px;height:675px;background:var(--bg);border-right:1px solid var(--border)}
.brand{left:11px;top:26px;width:128px;height:35px;border:2px solid var(--logo-border);border-radius:4px;background:#fafffa;display:flex;align-items:center;justify-content:center;font-weight:500;font-size:15px;color:var(--logo-green)}
.sidebar-rule{left:0;top:85px;width:150px;border-top:1px solid var(--border)}
.nav-link{left:25px;font-size:8.5px;color:var(--ink-soft)}
.nav-active{left:10px;top:112px;width:129px;height:20px;border-radius:3px;background:var(--active);color:#fff;font-size:8.5px;font-weight:500;padding-left:15px;line-height:20px}
.util{left:15px;font-size:8.5px;color:#333;display:flex;align-items:center;gap:6px}
.util i{width:8px;height:8px;border-radius:50%;background:#8a8f99;display:inline-block}

/* topbar */
.topbar{left:150px;top:0;width:1050px;height:46px;background:#f1f1f2;box-shadow:0 1px 2px rgba(0,0,0,.08)}
.page-title{left:175px;top:69px;font-size:15px;font-weight:500;color:#333}
.btn{top:71px;height:22px;border:1px solid var(--border);background:#fff;font-size:10px;display:flex;align-items:center;justify-content:center;color:var(--ink-soft);border-radius:1px}
.btn.primary{border-color:var(--primary);color:var(--primary)}

/* cards */
.card{background:var(--panel);border:1px solid var(--border);border-radius:3px}
.card-title{position:absolute;left:9px;top:8px;font-size:11.5px;font-weight:500;color:var(--navy)}

.legend{position:absolute;display:flex;align-items:center;gap:4px;font-size:9.5px;color:#222}
.legend b{width:12px;height:12px;display:inline-block}

.tl-legend{position:absolute;top:12px;font-size:7px;color:var(--ink-soft);display:flex;align-items:center;gap:4px}
.tl-legend i{width:6px;height:6px;border-radius:50%;display:inline-block}
.timeline{position:absolute;left:9px;top:33px;width:368px;height:13px;display:flex}
.ticks{position:absolute;left:9px;top:55px;width:368px;display:flex;justify-content:space-between;font-size:4.6px;color:#333}

.mini-table{position:absolute;left:9px;top:35px;width:368px;border:1px solid var(--border);font-size:9.5px;font-weight:500;color:#222}
.mini-row{display:grid;grid-template-columns:186px 1fr;height:23px;border-top:1px solid var(--border)}
.mini-row:first-child{border-top:none}
.mini-row span{padding-left:13px;line-height:23px}
.mini-row span+span{border-left:1px solid var(--border);font-weight:400}

.fill-row{position:absolute;left:9px;width:182px;display:flex;align-items:center;font-size:9.5px;color:var(--ink-soft)}
.fill-row i{width:8px;height:8px;border-radius:50%;margin-right:8px}
.fill-row em{margin-left:auto;font-style:normal;font-size:7.5px;color:#333}

/* tabs & table */
.tab{top:371px;height:23px;border:1px solid var(--border);background:#fff;font-size:11.5px;color:var(--ink-soft);display:flex;align-items:center;justify-content:center}
.tab.current{background:var(--active);border-color:var(--active);color:#fff}
.data-table{left:185px;top:407px;width:978px;height:169px;border:1px solid var(--border);border-radius:3px;background:#fff;font-size:10.5px;color:var(--ink-soft)}
.tr{display:grid;grid-template-columns:152px 114px 157px 157px 157px 157px 1fr;padding-left:13px;height:28px;align-items:center;border-top:1px solid var(--border)}
.tr.head{height:29px;border-top:none;background:#f7f7f8;color:#111;font-weight:500}
.status{display:inline-flex;align-items:center;gap:3px;font-size:10px;padding:0 5px;height:14px;border:1px solid}
.status i{width:4px;height:4px;border-radius:50%}
.pending{color:#e5303f;border-color:#f3b9be}.pending i{background:#e5303f}
.done{color:#3dbb3a;border-color:#b6e8b5}.done i{background:#3dbb3a}
.progress{color:#3f7fdc;border-color:#b9d0f3}.progress i{background:#3f7fdc}
</style>
</head>
<body>

<aside class="abs sidebar">
  <div class="abs brand">Logo</div>
  <div class="abs sidebar-rule"></div>
  <div class="abs nav-link" style="top:94px">Dashboard</div>
  <div class="abs nav-active">Machine States</div>
  <div class="abs nav-link" style="top:139px">Nav.......</div>
  <div class="abs util" style="top:596px"><i></i>Settings</div>
  <div class="abs util" style="top:616px"><i></i>About</div>
  <div class="abs util" style="top:636px"><i></i>Feedback</div>
</aside>

<header class="abs topbar"></header>

<h1 class="abs page-title">Sub Management</h1>
<div class="abs btn primary" style="left:734px;width:107px">Create Absence</div>
<div class="abs btn" style="left:846px;width:106px">Create Vacancy</div>
<div class="abs btn primary" style="left:957px;width:107px">Create Approve 8</div>
<div class="abs btn" style="left:1069px;width:106px">Approve 3</div>

<!-- Location overview chart -->
<section class="abs card" style="left:176px;top:106px;width:387px;height:238px">
  <div class="card-title">Location Overview</div>
  <svg class="abs" style="left:0;top:0" width="387" height="238" viewBox="0 0 620 381" font-family="Poppins, sans-serif">
    <text x="309" y="64" text-anchor="middle" font-size="16" fill="#777">Leave Request/ Openings/ Assignments</text>
    <g font-size="11" fill="#222" text-anchor="end">
      <text x="38" y="98">12</text><text x="38" y="133">10</text><text x="38" y="168">8</text>
      <text x="38" y="203">6</text><text x="38" y="238">4</text><text x="38" y="273">2,</text><text x="38" y="308">0</text>
    </g>
    <g stroke="#222" stroke-width="1">
      <line x1="50" y1="93" x2="50" y2="304"/>
      <line x1="50" y1="304" x2="620" y2="304"/>
      <line x1="44" y1="94" x2="50" y2="94"/><line x1="44" y1="129" x2="50" y2="129"/>
      <line x1="44" y1="164" x2="50" y2="164"/><line x1="44" y1="199" x2="50" y2="199"/>
      <line x1="44" y1="234" x2="50" y2="234"/><line x1="44" y1="269" x2="50" y2="269"/>
      <line x1="337" y1="304" x2="337" y2="310"/>
    </g>
    <rect x="84" y="241" width="65" height="59" fill="#5e3290"/>
    <rect x="84" y="231" width="65" height="10" fill="#2ea84a"/>
    <rect x="167" y="221" width="65" height="79" fill="#dc3545"/>
    <rect x="272" y="248" width="65" height="52" fill="#5e3290"/>
    <rect x="355" y="222" width="64" height="78" fill="#dc3545"/>
    <rect x="459" y="201" width="64" height="99" fill="#5e3290"/>
    <rect x="541" y="152" width="65" height="148" fill="#dc3545"/>
    <g font-size="11" fill="#222" text-anchor="middle">
      <text x="143" y="325">Lack Jonas Elementary</text>
      <text x="341" y="325">Festberg Middle Schoool</text>
      <text x="533" y="325">West Devante School</text>
    </g>
  </svg>
  <div class="legend" style="left:24px;top:213px"><b style="background:var(--purple-bar)"></b>Openings: Unfilled</div>
  <div class="legend" style="left:136px;top:213px"><b style="background:var(--green-bar)"></b>Openings: Filled</div>
  <div class="legend" style="left:238px;top:213px"><b style="background:var(--red-bar)"></b>Leave Request: Pending</div>
</section>

<!-- Today's summary -->
<section class="abs card" style="left:579px;top:106px;width:387px;height:70px">
  <div class="card-title">Toda's Summary</div>
  <div class="tl-legend" style="left:194px"><i style="background:var(--indigo)"></i>Running</div>
  <div class="tl-legend" style="left:256px"><i style="background:var(--violet)"></i>Stop</div>
  <div class="tl-legend" style="left:302px"><i style="background:var(--lilac)"></i>Stop</div>
  <div class="tl-legend" style="left:348px"><i style="background:var(--sky)"></i>Ideal</div>
  <div class="timeline">
    <span style="width:8.7%;background:var(--indigo)"></span>
    <span style="width:32.1%;background:var(--violet)"></span>
    <span style="width:19%;background:var(--lilac)"></span>
    <span style="width:40.2%;background:var(--sky)"></span>
  </div>
  <div class="ticks"><span>08:00</span><span>09:00</span><span>10:00</span><span>11:00</span><span>12:00</span><span>01:00</span><span>02:00</span><span>03:00</span><span>04:00</span><span>05:00</span><span>06:00</span><span>07:00</span><span>08:00</span></div>
</section>

<!-- Monthly summary -->
<section class="abs card" style="left:579px;top:192px;width:387px;height:152px">
  <div class="card-title">Monthly Summary</div>
  <div class="mini-table">
    <div class="mini-row"><span></span><span></span></div>
    <div class="mini-row"><span>Total Jobs</span><span>45</span></div>
    <div class="mini-row"><span>Filled Jobs</span><span>Data</span></div>
    <div class="mini-row"><span>No Sub Needed</span><span>Data</span></div>
  </div>
</section>

<!-- Monthly fill rate -->
<section class="abs card" style="left:982px;top:106px;width:193px;height:238px">
  <div class="card-title">Monthly Fill Rate</div>
  <svg class="abs" style="left:42px;top:48px" width="108" height="108" viewBox="0 0 170 170">
    <g transform="rotate(-96 85 85)" fill="none" stroke-width="43">
      <circle cx="85" cy="85" r="63.5" stroke="#3a2ec4"/>
      <circle cx="85" cy="85" r="63.5" stroke="#a59cf7" stroke-dasharray="132 399"/>
      <circle cx="85" cy="85" r="63.5" stroke="#6c63e8" stroke-dasharray="108 399" stroke-dashoffset="-132"/>
    </g>
  </svg>
  <div class="fill-row" style="top:180px"><i style="background:var(--indigo)"></i>Filled<em>40%</em></div>
  <div class="fill-row" style="top:198px"><i style="background:var(--violet)"></i>No Sub<em>27%</em></div>
  <div class="fill-row" style="top:217px"><i style="background:var(--lilac)"></i>Open<em>33%</em></div>
</section>

<!-- Requests table -->
<section class="abs card" style="left:174px;top:360px;width:1001px;height:227px"></section>
<div class="abs tab current" style="left:185px;width:124px">Location Overview</div>
<div class="abs tab" style="left:315px;width:174px">Regular Off Leave Requests</div>
<div class="abs tab" style="left:496px;width:150px">Pending Profile Images</div>
<div class="abs tab" style="left:652px;width:122px">My Leave Request</div>
<div class="abs tab" style="left:780px;width:148px">Substitute Attendance</div>

<div class="abs data-table">
  <div class="tr head"><span>Start Time</span><span>Duration</span><span>Reason</span><span>Message</span><span>Type</span><span>Category</span><span>Status</span></div>
  <div class="tr"><span>May 20, 2015</span><span>2 days 3hrs 30 mins</span><span>Error Code 123</span><span>Lit not locked</span><span>unplanned</span><span>Packaging</span><span><span class="status pending"><i></i>Pending</span></span></div>
  <div class="tr"><span>May 20, 2015</span><span>2 days 3hrs 30 mins</span><span>Error Code 123</span><span>Lit not locked</span><span>unplanned</span><span>Packaging</span><span><span class="status done"><i></i>Done</span></span></div>
  <div class="tr"><span>May 20, 2015</span><span>2 days 3hrs 30 mins</span><span>Error Code 123</span><span>Lit not locked</span><span>unplanned</span><span>Packaging</span><span><span class="status progress"><i></i>Progress</span></span></div>
  <div class="tr"><span>May 20, 2015</span><span>2 days 3hrs 30 mins</span><span>Error Code 123</span><span>Lit not locked</span><span>unplanned</span><span>Packaging</span><span><span class="status done"><i></i>Done</span></span></div>
  <div class="tr"><span>May 20, 2015</span><span>2 days 3hrs 30 mins</span><span>Error Code 123</span><span>Lit not locked</span><span>unplanned</span><span>Packaging</span><span><span class="status done"><i></i>Done</span></span></div>
</div>

</body>
</html>
```